Customer flyer

Hi there,

We need a flyer done for our father's business. It is called Tidal crest and the flyer will be distributed to realtors in British Columbia. He lends money to realtors when they have sold a home from the time subjects are removed from the transaction to when the sale closes. He is looking for a modern, classy look with the following information:

"Tidal Crest"

Realtor Pay Day upon Subject Removal

Did you know?

* Fees 100% tax deductable
* Same Day Service
* Confidential
* Low Rates

Your money from 738519 B.C. Ltd. and It can be directly deposited into your bank account or delivered to your office

For quote: call Gavin Merrow 250 555 0137

This is a small business so he doesn't have a logo and has never needed to do promotions before as it's run on word of mouth for the past 10 years. We are open to all ideas and suggestions - he is a finance guy so looking to you for the creative side :)

Thank you!

I don't like the phrase Realtor Pay Day upon subject removal. I think I prefer "Realtors! Celebrate Your Home sales upon subject removal" . Your thoughts?

Thank you

```html
<!DOCTYPE html>
<html lang="en">
<head>
<meta charset="utf-8">
<title>Tidal Crest – Realtor Pay Day</title>
<link rel="stylesheet" href="https://fonts.googleapis.com/css2?family=Coustard:wght@900&family=Jost:wght@300;400&family=Roboto:wght@700;900&display=swap">
<style>
  :root{
    --cream:#fdfbe1;
    --navy:#0f2a6b;
    --ink-blue:#1c3c86;
    --sky:#1f77c4;
    --sky-light:#74b7e6;
    --sky-deep:#1a5aa8;
    --yellow:#f7ee1a;
    --red:#e8282a;
    --photo-cash:#9fb48a;
    --photo-chrome:#cfcab8;
  }
  *{margin:0;padding:0;box-sizing:border-box}
  html,body{width:848px;height:1200px;overflow:hidden;background:var(--cream)}
  .flyer{position:relative;width:848px;height:1200px;background:var(--cream);overflow:hidden}
  .sky-wave{position:absolute;left:0;top:0;width:848px;height:460px}
  .brand{
    position:absolute;left:88px;top:52px;
    font-family:"Coustard",Georgia,serif;font-weight:900;
    font-size:98px;line-height:100px;color:var(--navy);
    -webkit-text-stroke:0;
    text-shadow:3px 0 #fff,-3px 0 #fff,0 3px #fff,0 -3px #fff,2px 2px #fff,-2px -2px #fff,2px -2px #fff,-2px 2px #fff;
  }
  .payday{
    position:absolute;right:60px;top:258px;text-align:left;
    font-family:"Coustard",Georgia,serif;font-weight:900;
    font-size:62px;line-height:74px;color:var(--yellow);
    -webkit-text-stroke:2px var(--navy);paint-order:stroke fill;
  }
  .payday .line{display:block}
  .payday .line + .line{padding-left:0}
  .subject{
    position:absolute;right:40px;top:418px;
    font-family:"Roboto",Arial,sans-serif;font-weight:700;
    font-size:24px;color:var(--sky);
  }
  .cash-visual{
    position:absolute;left:21px;top:318px;width:330px;height:352px;
    background:radial-gradient(ellipse at 55% 28%,var(--photo-cash) 0 30%,transparent 55%),
               linear-gradient(180deg,transparent 0 45%,var(--photo-chrome) 60%,#b9b29b 100%);
    border-radius:18px;opacity:.9;
  }
  .facts{position:absolute;left:373px;top:476px}
  .facts h2{
    font-family:"Roboto",Arial,sans-serif;font-weight:900;
    font-size:37px;color:var(--navy);margin-bottom:6px;
  }
  .facts ul{list-style:none}
  .facts li{
    font-family:"Jost",Arial,sans-serif;font-weight:300;
    font-size:31px;line-height:41px;color:var(--navy);
  }
  .facts li::before{content:"\2731";color:var(--red);font-size:22px;margin-right:10px;vertical-align:3px}
  .details{
    position:absolute;left:110px;width:600px;top:742px;text-align:center;
    font-family:"Jost",Arial,sans-serif;font-weight:400;
    font-size:29px;line-height:41px;color:var(--ink-blue);
  }
  .contact{position:absolute;left:0;width:848px;top:958px;text-align:center;padding-right:0}
  .contact .prompt{
    font-family:"Jost",Arial,sans-serif;font-weight:400;font-size:44px;line-height:56px;color:var(--navy);
  }
  .contact .name{
    font-family:"Roboto",Arial,sans-serif;font-weight:900;font-size:58px;line-height:70px;color:var(--navy);
  }
  .contact .phone{
    font-family:"Roboto",Arial,sans-serif;font-weight:900;font-size:66px;line-height:84px;color:var(--navy);letter-spacing:1px;
  }
  .contact-inner{width:600px;margin-left:126px}
</style>
</head>
<body>
<main class="flyer">
  <svg class="sky-wave" viewBox="0 0 848 460" aria-hidden="true">
    <defs>
      <radialGradient id="skyGlow" cx="0.3" cy="0.35" r="0.85">
        <stop offset="0" stop-color="var(--sky-light)" style="stop-color:#7dbde9"/>
        <stop offset="0.6" stop-color="#3f8fd2"/>
        <stop offset="1" stop-color="#1a5aa8"/>
      </radialGradient>
      <linearGradient id="crestBand" x1="0" y1="0" x2="1" y2="0">
        <stop offset="0" stop-color="#ffffff" stop-opacity=".15"/>
        <stop offset="1" stop-color="#d8ecf8" stop-opacity=".8"/>
      </linearGradient>
    </defs>
    <path d="M0 0H848V270C760 250 650 240 560 262C460 286 400 330 320 336C220 344 120 350 0 352Z" fill="url(#skyGlow)"/>
    <path d="M0 352C120 350 220 344 320 336C400 330 460 286 560 262C650 240 760 250 848 270V290C760 266 660 262 570 282C470 304 410 345 320 352C220 360 110 362 0 364Z" fill="url(#crestBand)"/>
  </svg>

  <h1 class="brand">Tidal<br>Crest</h1>

  <p class="payday"><span class="line">Realtor</span><span class="line">Pay Day</span></p>
  <p class="subject">upon Subject Removal</p>

  <div class="cash-visual" role="img" aria-label="Photo of a hand holding a fan of banknotes above large chrome 3D letters reading Good Credit"></div>

  <section class="facts">
    <h2>Did you know?</h2>
    <ul>
      <li>Fees 100% tax deductable</li>
      <li>Same Day Service</li>
      <li>Confidential</li>
      <li>Low Rates</li>
    </ul>
  </section>

  <p class="details">Your money from 738519 B.C. Ltd.<br>and It can be directly deposited into<br>your bank account or<br>delivered to your office</p>

  <section class="contact">
    <div class="contact-inner">
      <p class="prompt">For quote: call</p>
      <p class="name">Gavin Merrow</p>
      <p class="phone">250 555 0137</p>
    </div>
  </section>
</main>
</body>
</html>
```